Coldforge Prime manufacturing Project

We are looking at getting a brand new design for a new company that deals in selling stainless tubing and other stainless still products such as handrails, Spigots, Balustrade Fittings
Glass, Glass fittings and Aluminium Channels

We require a very clean website that deals with the following colours:

Blue to light blues
Blacks
Greys to light Greys
Whites

We are open for other ideas BUT we *DO NOT* want any pinks, greens or bright colours except for backgrounds colours we have chosen above. (It can be solid, gradient or a subtle pattern)

YOU MUST KEEP THE LOGO AS IS. PLEASE DO NOT ALTER THE LOGO IN *ANY WAY* and the logo MUST be the same colours and fonts.

Logo is attached.

The site must contain these aspects:
jQuery Slider (Image slide show)
Top drop down Menus
Be no more than 900px wide
Text is to be to the w3C standards. (no special fonts)

We will chop up the design into html format. You just need to provide the PSD file.

The clients opposition is:
www.quorvatrim.example

Industry/Entity Type

It Company

Requirements
Nice to have
• Alter the logo in anyway

Files

```html
<!DOCTYPE html>
<html lang="en">
<head>
<meta charset="utf-8">
<title>Coldforge Prime – Stainless Railing &amp; Glass Systems</title>
<link href="https://fonts.googleapis.com/css2?family=Arimo:wght@400;700&family=Open+Sans:wght@600;700&family=Ubuntu:wght@400;500;700&display=swap" rel="stylesheet">
<style>
  :root{
    --band-top:#e4e4e4;
    --band-bottom:#c9c9c9;
    --blue:#5a6ea3;
    --blue-light:#7285b8;
    --blue-dark:#3f5186;
    --ink:#333333;
    --white:#ffffff;
    --label:#2e2e2e;
    --footer:#3a3a3a;
  }
  *{margin:0;padding:0;box-sizing:border-box}
  html,body{width:1146px;height:1200px;overflow:hidden;background:var(--white)}
  body{position:relative;font-family:"Arimo",Arial,sans-serif;color:var(--ink)}
  .top-band{position:absolute;left:0;top:0;width:1146px;height:382px;
    background:radial-gradient(ellipse at 25% 10%,#f2f2f2 0%,var(--band-top) 25%,var(--band-bottom) 70%)}
  .brand{position:absolute;left:131px;top:29px;display:flex;align-items:center;gap:10px}
  .brand-dot{width:86px;height:86px;border-radius:50%;background:#1f2530}
  .brand-name{font-family:"Ubuntu",sans-serif;font-weight:400;color:#1c1c1c;line-height:1.15}
  .brand-name .main{display:block;font-size:22px}
  .brand-name .sub{display:block;font-size:11px;letter-spacing:2px;padding-left:18px}
  .search{position:absolute;left:800px;top:58px;width:205px;height:34px;background:var(--white);
    border:1px solid #c4c4c4;display:flex;align-items:center}
  .search span{flex:1;padding-left:8px;font-size:13px;color:#9a9a9a;letter-spacing:.5px}
  .search i{width:34px;height:32px;border-left:1px solid #ddd;display:flex;align-items:center;justify-content:center}
  .main-nav{position:absolute;left:124px;top:131px;width:884px;height:42px;border-radius:8px;
    background:linear-gradient(var(--blue-light),var(--blue) 55%,#52669c);border:1px solid var(--blue-dark)}
  .main-nav a{position:absolute;top:0;line-height:40px;font-family:"Open Sans",sans-serif;font-weight:700;
    font-size:12px;color:var(--white);text-decoration:none;letter-spacing:.3px;white-space:nowrap}
  .main-nav .sep{position:absolute;top:8px;width:1px;height:26px;background:#3e4f80;box-shadow:1px 0 0 #8797c3}
  .slider{position:absolute;left:124px;top:192px;width:884px;height:338px;background:var(--white);
    border-radius:8px;box-shadow:0 10px 14px -8px rgba(0,0,0,.35)}
  .slide-photo{position:absolute;left:7px;top:8px;width:872px;height:323px;border-radius:6px;
    background:
      radial-gradient(ellipse 30% 45% at 80% 45%,rgba(255,255,255,.75),rgba(255,255,255,0) 70%),
      radial-gradient(ellipse 40% 30% at 30% 85%,rgba(150,145,135,.35),rgba(150,145,135,0) 70%),
      linear-gradient(180deg,rgba(255,255,255,.25) 0%,rgba(255,255,255,0) 35%,rgba(0,0,0,.06) 100%),
      linear-gradient(100deg,#cfcbc3 0%,#c2bdb4 35%,#dcd9d3 62%,#e9e7e3 80%,#d6d3cd 100%);
    box-shadow:inset 0 0 0 1px rgba(0,0,0,.06)}
  .slide-caption{position:absolute;left:26px;font-family:"Arimo",sans-serif;font-weight:700;font-size:19px;
    color:#6a6a6a;text-shadow:1px 1px 0 #fff,-1px -1px 0 rgba(0,0,0,.15);letter-spacing:.3px}
  .welcome{position:absolute;left:131px;top:571px;width:470px}
  .welcome h1{font-family:"Ubuntu",sans-serif;font-weight:400;font-size:24px;color:#2a2a2a;letter-spacing:.6px}
  .welcome h1 em{font-style:normal;color:var(--blue)}
  .welcome p{margin-top:11px;padding-left:2px;width:456px;font-size:12.2px;line-height:19.1px;color:var(--ink)}
  .welcome p + p{margin-top:19px}
  .btn-more{position:absolute;left:509px;top:789px;width:86px;height:26px;border-radius:4px;
    background:linear-gradient(var(--blue-light),var(--blue));border:1px solid var(--blue-dark);
    color:var(--white);font-family:"Arimo",sans-serif;font-weight:700;font-size:10.5px;
    text-align:center;line-height:24px;letter-spacing:.3px}
  .welcome-photo{position:absolute;left:616px;top:573px;width:390px;height:243px;border:1px solid #c8c8c8;padding:3px}
  .welcome-photo div{width:100%;height:100%;
    background:
      radial-gradient(ellipse 35% 25% at 40% 15%,rgba(160,170,180,.45),rgba(160,170,180,0) 70%),
      radial-gradient(ellipse 40% 25% at 55% 50%,rgba(176,150,90,.45),rgba(176,150,90,0) 70%),
      radial-gradient(ellipse 45% 22% at 50% 80%,rgba(150,135,120,.45),rgba(150,135,120,0) 70%),
      linear-gradient(180deg,#3b302c 0%,#5a524e 30%,#6e6862 60%,#767069 100%)}
  .products-bar{position:absolute;left:124px;top:856px;width:884px;height:36px;background:var(--blue)}
  .products-bar h2{position:absolute;left:13px;top:6px;font-family:"Ubuntu",sans-serif;font-weight:700;
    font-size:19px;color:var(--white);letter-spacing:.4px}
  .products-bar .more{position:absolute;right:14px;top:10px;font-family:"Ubuntu",sans-serif;font-weight:500;
    font-size:14px;color:var(--white);display:flex;align-items:center;gap:6px}
  .product{position:absolute;top:906px;width:266px}
  .product .photo{height:202px;box-shadow:inset 0 0 0 1px rgba(0,0,0,.05)}
  .product .label{margin-top:2px;height:31px;background:var(--label);color:var(--white);text-align:center;
    font-family:"Open Sans",sans-serif;font-weight:700;font-size:16.5px;line-height:31px;letter-spacing:1px}
  .site-footer{position:absolute;left:0;top:1165px;width:1146px;height:35px;background:var(--footer);
    color:var(--white);font-size:12px;text-align:center;line-height:35px}
</style>
</head>
<body>
  <div class="top-band"></div>

  <header>
    <div class="brand">
      <span class="brand-dot"></span>
      <span class="brand-name"><span class="main">Coldforge Prime</span><span class="sub">Manufacturing Co. Ltd</span></span>
    </div>
    <div class="search">
      <span>Search Velmora</span>
      <i><svg width="20" height="20" viewBox="0 0 20 20"><circle cx="12" cy="8" r="5.5" fill="none" stroke="#222" stroke-width="2"/><line x1="8" y1="12" x2="3" y2="17" stroke="#222" stroke-width="2.5" stroke-linecap="round"/></svg></i>
    </div>
    <nav class="main-nav">
      <a style="left:24px">HOME</a><span class="sep" style="left:86px"></span>
      <a style="left:112px">ABOUT VELMORA</a><span class="sep" style="left:236px"></span>
      <a style="left:259px">PRODUCTS</a><span class="sep" style="left:355px"></span>
      <a style="left:378px">DOWNLOAD</a><span class="sep" style="left:481px"></span>
      <a style="left:505px">CONTACT US</a>
    </nav>
  </header>

  <section class="slider">
    <div class="slide-photo" role="img" aria-label="Stainless steel stair railing with horizontal rods beside white floating stairs"></div>
    <div class="slide-caption" style="top:24px">STAINLESS STEEL RAILING</div>
    <div class="slide-caption" style="top:71px">&amp; GLASS SYSTEMS</div>
  </section>

  <section class="welcome">
    <h1><em>Welcome</em> to Velmora...</h1>
    <p>simply dummy text of the printing and typesetting industry. Lorem Ipsum has been the industry's standard dummy text ever since the 1500s, when an unknown printer took a galley of type and scrambled it to make a type specimen book. It has sur-vived not only five centuries, but also the leap into electronic typesetting,</p>
    <p>Remaining essentially unchanged. It was popularised in the 1960s with the release of Letraset sheets containing Lorem Ipsum passages, and more recently with desk-top publishing software</p>
  </section>
  <div class="btn-more">READ MORE</div>
  <figure class="welcome-photo"><div role="img" aria-label="Assorted brass and metal taps laid on a wooden surface"></div></figure>

  <section>
    <div class="products-bar">
      <h2>Velmora Products</h2>
      <span class="more">more <svg width="14" height="12" viewBox="0 0 14 12"><path d="M1 1l5 5-5 5M7 1l5 5-5 5" fill="none" stroke="#fff" stroke-width="2.2"/></svg></span>
    </div>
    <div class="product" style="left:125px">
      <div class="photo" role="img" aria-label="Stainless steel handrail on a wall bracket" style="background:radial-gradient(ellipse 30% 25% at 45% 75%,rgba(60,60,60,.35),rgba(60,60,60,0) 70%),linear-gradient(160deg,#7d7d7d 0%,#a9a9a9 30%,#bdbdbd 55%,#a3a3a3 80%,#8e8e8e 100%)"></div>
      <div class="label">HANDRAILS</div>
    </div>
    <div class="product" style="left:433px">
      <div class="photo" role="img" aria-label="Glass balustrade with stainless posts on a mezzanine floor" style="background:radial-gradient(ellipse 25% 40% at 95% 40%,rgba(200,190,170,.6),rgba(200,190,170,0) 70%),linear-gradient(#ece8e7 0%,#dcd9d6 45%,#cfccc8 58%,#d2ab5c 66%,#c79f4c 85%,#4f5a3e 100%)"></div>
      <div class="label">GLASS FITTINGS</div>
    </div>
    <div class="product" style="left:742px">
      <div class="photo" role="img" aria-label="Aluminium channel profiles in assorted finishes" style="background:radial-gradient(ellipse 45% 40% at 75% 60%,rgba(170,160,150,.35),rgba(170,160,150,0) 70%),linear-gradient(135deg,#ebe9e8 0%,#dedbd9 45%,#cfcac6 75%,#c6c1bc 100%)"></div>
      <div class="label">ALUMINIUM CHANNELS</div>
    </div>
  </section>

  <footer class="site-footer">Copyright (c) VELMORA. All Rights Reserved.</footer>
</body>
</html>
```